A Student Forum developed (or Plugin tweaked) and installed on our current Wordpress Website

We require a Student Forum with LOGIN from our current Website.

Current website reference : www.harrowvaleskills.edu.au

The student forum is for students to ask questions about their studies and for ADMINS to reply.

The student forum should be able to cater for development of CATEGORIES. I have included a picture shot of the old forum in Joomla for understanding.

This job includes the overall design and also installation. It is perfectly fine, if the user sources a suitable Plugin as the basis of the forum, tweaks it to our branding and installs.

Please review the general look and feel of the website for branding.

Target Market(s)

Students

Industry/Entity Type

Education

Font styles to use
Sans Serif

Colors
ffffff

Requirements
Must have
• Categories in Forum - levels of administration
Nice to have
• uploads and downloads would be good
• place for student photo
• News etc.

```html
<!DOCTYPE html>
<html lang="en">
<head>
<meta charset="utf-8">
<title>Kestrel Forum : Category Manager</title>
<link href="https://fonts.googleapis.com/css2?family=Open+Sans:wght@300;400;600&display=swap" rel="stylesheet">
<style>
:root{
  --navy:#263a5a;
  --navy-deep:#1c2b45;
  --orange:#e7962f;
  --panel:#e6e6e6;
  --panel-light:#f2f2f2;
  --tag-bg:#e1e1e1;
  --line:#c9c9c9;
  --link:#1a5eb8;
  --text:#333;
  --muted:#555;
  --red:#d0311e;
  --green:#1e9a3c;
  --white:#fff;
}
*{box-sizing:border-box;margin:0;padding:0}
html,body{width:1200px;height:1092px;overflow:hidden;background:var(--white)}
body{position:relative;font-family:"Open Sans",Arial,sans-serif;color:var(--text);font-size:11px}
.abs{position:absolute}

/* header */
.brand{left:34px;top:24px;width:100px;display:flex;flex-direction:column;align-items:center;gap:6px}
.brand-mark{width:44px;height:44px;background:var(--navy)}
.brand-name{color:var(--navy);font-weight:600;font-size:9px;line-height:11px;text-align:center;letter-spacing:.4px}
.login-title{left:778px;top:22px;font-size:15px;color:var(--navy)}
.field{border:1px solid #ccc;background:var(--white);height:24px;padding:0 8px;display:flex;align-items:center;font-size:10px;color:var(--muted)}
.btn{height:24px;display:flex;align-items:center;justify-content:center;color:var(--white);font-size:10px;font-weight:600}
.btn-login{left:1056px;top:50px;width:50px;background:var(--navy)}
.btn-register{left:1117px;top:50px;width:66px;background:var(--orange)}
.site-search{left:780px;top:88px;width:403px;background:#f3f3f3;justify-content:space-between}

/* nav */
.mainnav{left:0;top:136px;width:1200px;height:39px;background:var(--navy);display:flex;padding-left:36px}
.mainnav a{color:#c8d0dc;font-size:12px;text-decoration:none;display:flex;align-items:center;padding:0 13px}
.mainnav a.active{background:var(--navy-deep);color:var(--white);padding:0 20px 0 15px}

/* page title */
.page-title{left:37px;top:192px;font-size:22px;color:var(--navy-deep);font-weight:400}
.title-rule{left:21px;top:229px;width:925px;height:1px;background:var(--line)}
.toolbar{left:37px;top:240px;display:flex;gap:31px;font-size:14px;color:#444}
.toolbar span{display:flex;align-items:center;gap:5px}
.toolbar svg{width:12px;height:12px}

/* manager panel */
.panel{left:17px;top:273px;width:934px;height:763px;background:var(--panel)}
.search-row{left:51px;top:288px;display:flex;gap:8px}
.search-row .field{height:32px;font-size:11px;padding:0 14px}
.btn-dark{background:var(--navy);width:46px;height:32px;font-weight:400;font-size:11px}
.sort-row{left:453px;top:288px;display:flex;gap:8px}
.select{border:1px solid #ccc;background:var(--white);width:115px;height:32px;display:flex;align-items:center;justify-content:space-between;padding:0 10px 0 14px;font-size:11px;color:var(--muted)}
.select svg,.mini svg{width:7px;height:5px}
.head-row{left:17px;top:338px;width:934px;height:48px;background:var(--panel-light)}
.grid{display:grid;grid-template-columns:30px 42px 35px 467px 84px 84px 84px 84px;align-items:center}
.table-head{left:28px;top:338px;height:48px;font-size:11px}
.table-head .lbl{color:var(--link);text-align:center}
.table-head .anon{color:#222}
.status-h{grid-column:1/3;display:flex;align-items:center;gap:6px;padding-left:8px;color:var(--link)}
.cb{width:9px;height:9px;border:1px solid #aaa;background:var(--white);justify-self:center}
.filter-row{left:28px;top:386px;height:46px}
.mini{width:53px;height:24px;border:1px solid #bbb;background:var(--white);display:flex;align-items:center;justify-content:space-between;padding:0 8px;font-size:10px;color:#444;justify-self:center}
.filter-row .status-f{grid-column:1/3;margin-left:24px;justify-self:start}
.title-f{grid-column:4/5;width:370px;height:24px;border:1px solid #bbb;background:var(--white);display:flex;align-items:center;padding:0 10px;font-size:10px;color:#666}

.rows{left:28px;top:432px;width:913px;display:flex;flex-direction:column;gap:5.8px}
.row{height:48px;background:var(--white)}
.row .ic{width:13px;height:13px;justify-self:center}
.row .title{grid-column:4/5;font-size:9.6px;line-height:15.5px;color:#333;padding-right:10px}
.row .title a{color:var(--link);text-decoration:none}
.row .sec{font-size:9.6px;color:#333;justify-self:center;align-self:start;margin-top:10px}

/* sidebar */
.sidemenu{left:968px;top:189px;width:215px;background:var(--navy)}
.sidemenu li{list-style:none;height:38.4px;display:flex;align-items:center;gap:12px;padding-left:20px;color:var(--white);font-size:14.5px;font-weight:300;border-bottom:1px solid #34496b}
.sidemenu li.active{background:var(--navy-deep)}
.sidemenu li:last-child{border-bottom:none;height:41px}
.sidemenu svg{width:13px;height:13px;fill:#dfe4ec}
.tags{left:968px;top:595px;width:215px;height:441px;background:var(--tag-bg)}
.tags h2{background:var(--navy-deep);color:var(--white);font-size:14.5px;font-weight:300;height:39px;display:flex;align-items:center;padding-left:18px}
.tags li{list-style:none;height:54px;border-bottom:1px solid #c9c9c9;padding:11px 14px 0 17px;font-size:9.8px;line-height:15.5px;color:#444}
.tags li:last-child{border-bottom:none}

.footer{left:0;top:1053px;width:856px;text-align:center;font-size:11.5px;color:#444}
</style>
</head>
<body>
<svg width="0" height="0" style="position:absolute">
  <defs>
    <symbol id="ok" viewBox="0 0 16 16"><circle cx="8" cy="8" r="8" fill="#1e9a3c"/><path d="M4.3 8.3l2.5 2.5 4.9-5" stroke="#fff" stroke-width="2" fill="none"/></symbol>
    <symbol id="off" viewBox="0 0 16 16"><circle cx="8" cy="8" r="6.6" fill="none" stroke="#d0311e" stroke-width="2"/><circle cx="8" cy="8" r="2.6" fill="#d0311e"/></symbol>
    <symbol id="caret" viewBox="0 0 8 5"><path d="M1 1l3 3 3-3" stroke="#555" fill="none" stroke-width="1.2"/></symbol>
  </defs>
</svg>

<header>
  <div class="abs brand">
    <span class="brand-mark"></span>
    <span class="brand-name">HARROWVALE INSTITUTE OF TRAINING</span>
  </div>
  <div class="abs login-title">Student Login</div>
  <div class="abs field" style="left:779px;top:50px;width:134px">Username</div>
  <div class="abs field" style="left:917px;top:50px;width:134px">Password</div>
  <div class="abs btn btn-login">LOGIN</div>
  <div class="abs btn btn-register">REGISTER</div>
  <div class="abs field site-search">Search
    <svg width="11" height="11" viewBox="0 0 12 12"><circle cx="5" cy="5" r="3.8" fill="none" stroke="#333" stroke-width="1.6"/><path d="M8 8l3 3" stroke="#333" stroke-width="1.8"/></svg>
  </div>
</header>

<nav class="abs mainnav">
  <a class="active">Topics</a><a>Subjects</a><a>Books</a><a>Education</a><a>Videos</a><a>Help</a><a>Live Chat</a>
</nav>

<main>
  <h1 class="abs page-title">Kestrel Forum : Category Manager</h1>
  <div class="abs title-rule"></div>
  <div class="abs toolbar">
    <span><svg viewBox="0 0 12 12"><circle cx="6" cy="6" r="6" fill="#444"/><path d="M6 3v6M3 6h6" stroke="#fff" stroke-width="1.6"/></svg>New Category</span>
    <span><svg viewBox="0 0 12 12"><rect x="1" y="2" width="8" height="9" fill="none" stroke="#444" stroke-width="1.2"/><path d="M5 7l6-6" stroke="#444" stroke-width="1.8"/></svg>Edit</span>
    <span><svg viewBox="0 0 12 12"><circle cx="6" cy="6" r="6" fill="#444"/><path d="M3.2 6.2l1.9 1.9 3.7-3.8" stroke="#fff" stroke-width="1.5" fill="none"/></svg>Publish</span>
    <span><svg viewBox="0 0 12 12"><circle cx="6" cy="6" r="5" fill="none" stroke="#444" stroke-width="1.6"/><circle cx="6" cy="6" r="2" fill="#444"/></svg>Unpublish</span>
    <span><svg viewBox="0 0 12 12"><circle cx="6" cy="6" r="6" fill="#444"/><path d="M4 4l4 4M8 4l-4 4" stroke="#fff" stroke-width="1.5"/></svg>Delete</span>
  </div>

  <section>
    <div class="abs panel"></div>
    <div class="abs search-row">
      <div class="field" style="width:192px">Search</div>
      <div class="btn btn-dark">Filter</div>
      <div class="btn btn-dark" style="margin-left:-2px">Reset</div>
    </div>
    <div class="abs sort-row">
      <div class="select">Reorder<svg><use href="#caret"/></svg></div>
      <div class="select">Ascending<svg><use href="#caret"/></svg></div>
      <div class="select">20<svg><use href="#caret"/></svg></div>
      <div class="select">Access<svg><use href="#caret"/></svg></div>
    </div>

    <div class="abs head-row"></div>
    <div class="abs grid table-head">
      <div class="status-h"><span class="cb" style="justify-self:auto"></span>Status</div>
      <div></div>
      <div class="lbl" style="text-align:left;color:var(--link)">Title</div>
      <div class="lbl">Locked</div><div class="lbl">Review</div><div class="lbl">Polls</div><div class="lbl anon">Anonymous</div>
    </div>

    <div class="abs grid filter-row">
      <div class="mini status-f">All<svg><use href="#caret"/></svg></div>
      <div></div>
      <div class="title-f">Filter</div>
      <div class="mini">All<svg><use href="#caret"/></svg></div>
      <div class="mini">All<svg><use href="#caret"/></svg></div>
      <div class="mini">All<svg><use href="#caret"/></svg></div>
      <div class="mini">All<svg><use href="#caret"/></svg></div>
    </div>

    <div class="abs rows">
      <div class="row grid"><span class="cb"></span><svg class="ic"><use href="#ok"/></svg><span></span><p class="title"><a>Vestibulum condimentum, risus ut posuere cursus, velit justo accumsan</a> sem, lobortis aliquet metus dui eu libero</p><svg class="ic"><use href="#off"/></svg><span></span><span class="sec">Section</span><span></span></div>
      <div class="row grid"><span class="cb"></span><svg class="ic"><use href="#off"/></svg><span></span><p class="title"><a>Aenean facilisis tincidunt lectus, id dictum nisi luctu</a>, velit justo accumsan sem, lobortis aliquet metus dui eu libero</p><svg class="ic"><use href="#off"/></svg><svg class="ic"><use href="#off"/></svg><svg class="ic"><use href="#off"/></svg><svg class="ic"><use href="#off"/></svg></div>
      <div class="row grid"><span class="cb"></span><svg class="ic"><use href="#ok"/></svg><span></span><p class="title"><a>Fusce sollicitudin lorem et luctus volutpat</a> justo accumsan sem, lobortis aliquet metus dui eu libero placerat dapibus gravida</p><svg class="ic"><use href="#off"/></svg><svg class="ic"><use href="#off"/></svg><svg class="ic"><use href="#off"/></svg><svg class="ic"><use href="#off"/></svg></div>
      <div class="row grid"><span class="cb"></span><svg class="ic"><use href="#ok"/></svg><span></span><p class="title"><a>Aenean facilisis tincidunt lectus, id dictum nisi luctu</a>, velit justo accumsan sem, lobortis aliquet metus dui eu libero</p><svg class="ic"><use href="#off"/></svg><svg class="ic"><use href="#off"/></svg><svg class="ic"><use href="#off"/></svg><svg class="ic"><use href="#off"/></svg></div>
      <div class="row grid"><span class="cb"></span><svg class="ic"><use href="#off"/></svg><span></span><p class="title"><a>Fusce sollicitudin lorem et luctus volutpat</a> justo accumsan sem, lobortis aliquet metus dui eu libero placerat dapibus gravida</p><svg class="ic"><use href="#off"/></svg><svg class="ic"><use href="#off"/></svg><svg class="ic"><use href="#off"/></svg><svg class="ic"><use href="#off"/></svg></div>
      <div class="row grid"><span class="cb"></span><svg class="ic"><use href="#off"/></svg><span></span><p class="title"><a>Aenean facilisis tincidunt lectus, id dictum nisi luctu</a>, velit justo accumsan sem, lobortis aliquet metus dui eu libero</p><svg class="ic"><use href="#off"/></svg><svg class="ic"><use href="#off"/></svg><svg class="ic"><use href="#off"/></svg><svg class="ic"><use href="#off"/></svg></div>
      <div class="row grid"><span class="cb"></span><svg class="ic"><use href="#off"/></svg><span></span><p class="title"><a>Fusce sollicitudin lorem et luctus volutpat</a> justo accumsan sem, lobortis aliquet metus dui eu libero placerat dapibus gravida</p><svg class="ic"><use href="#off"/></svg><svg class="ic"><use href="#off"/></svg><svg class="ic"><use href="#off"/></svg><svg class="ic"><use href="#off"/></svg></div>
      <div class="row grid"><span class="cb"></span><svg class="ic"><use href="#off"/></svg><span></span><p class="title"><a>Aenean facilisis tincidunt lectus, id dictum nisi luctu</a>, velit justo accumsan sem, lobortis aliquet metus dui eu libero</p><svg class="ic"><use href="#off"/></svg><svg class="ic"><use href="#off"/></svg><svg class="ic"><use href="#off"/></svg><svg class="ic"><use href="#off"/></svg></div>
      <div class="row grid"><span class="cb"></span><svg class="ic"><use href="#off"/></svg><span></span><p class="title"><a>Fusce sollicitudin lorem et luctus volutpat</a> justo accumsan sem, lobortis aliquet metus dui eu libero placerat dapibus gravida</p><svg class="ic"><use href="#ok"/></svg><span></span><span class="sec">Section</span><span></span></div>
      <div class="row grid"><span class="cb"></span><svg class="ic"><use href="#ok"/></svg><span></span><p class="title"><a>Aenean facilisis tincidunt lectus, id dictum nisi luctu</a>, velit justo accumsan sem, lobortis aliquet metus dui eu libero</p><svg class="ic"><use href="#ok"/></svg><svg class="ic"><use href="#off"/></svg><svg class="ic"><use href="#off"/></svg><svg class="ic"><use href="#off"/></svg></div>
      <div class="row grid"><span class="cb"></span><svg class="ic"><use href="#off"/></svg><span></span><p class="title"><a>Fusce sollicitudin lorem et luctus volutpat</a> justo accumsan sem, lobortis aliquet metus dui eu libero placerat dapibus gravida</p><svg class="ic"><use href="#ok"/></svg><svg class="ic"><use href="#off"/></svg><svg class="ic"><use href="#off"/></svg><svg class="ic"><use href="#off"/></svg></div>
    </div>
  </section>
</main>

<aside>
  <ul class="abs sidemenu">
    <li><svg viewBox="0 0 14 14"><path d="M1 11a6 6 0 0 1 12 0z"/></svg>Dashboard</li>
    <li class="active"><svg viewBox="0 0 14 14"><circle cx="7" cy="4" r="3.3"/><path d="M1 13c0-4 12-4 12 0z"/></svg>Category Manager</li>
    <li><svg viewBox="0 0 14 14"><path d="M0 3h5l1 1.5h7V12H0z"/></svg>File Manager</li>
    <li><svg viewBox="0 0 14 14"><circle cx="7" cy="7" r="6.5"/></svg>Emoticon Manager</li>
    <li><svg viewBox="0 0 14 14"><path d="M7 0.5l2 4.3 4.6.5-3.4 3.1 1 4.6L7 10.6 2.8 13l1-4.6L.4 5.3 5 4.8z"/></svg>Rank Manager</li>
    <li><svg viewBox="0 0 14 14"><path d="M13 1L6 9l-1-1zM4.5 8.5l1 1c0 2-2 3.5-4.5 3 1.5-1 1-3.5 3.5-4z"/></svg>Template Manager</li>
    <li><svg viewBox="0 0 14 14"><circle cx="7" cy="7" r="6.5"/><path d="M7 3v4h3" stroke="#263a5a" stroke-width="1.6" fill="none"/></svg>Configuration</li>
    <li><svg viewBox="0 0 14 14"><circle cx="5" cy="8" r="4"/><circle cx="11" cy="4" r="2.6"/><circle cx="11" cy="11" r="2"/></svg>Plug-in Manager</li>
    <li><svg viewBox="0 0 14 14"><path d="M1 12l6-6a3.5 3.5 0 1 1 1 1l-6 6z"/></svg>Forum Tools</li>
    <li><svg viewBox="0 0 14 14"><path d="M2 2h10v1.5H2zM5 0.5h4V2H5zM3 4h8l-.7 9.5H3.7z"/></svg>Trash Manager</li>
  </ul>
  <div class="abs tags">
    <h2>Popular Tags</h2>
    <ul>
      <li>Quisque aliquet ex nec est vestibulum pulvinar convallis molestie enim</li>
      <li>Vivamus lacus justo, ultrices nec erat in, euismod iaculis mauris</li>
      <li>Fusce vitae lectus sit amet mi pulvinar maximus. Aenean placerat.</li>
      <li>Vestibulum ante ipsum primis in faucibus orci luctus et ultrices posuere</li>
      <li>Vestibulum eget nisl metus. Phasellus nisl est, condimentum vitae faucibus</li>
      <li>Nunc sit amet consequat risus. Curabitur ac elit leo. In eleifend dui</li>
      <li>Integer eu massa lacinia, lacinia nulla non, volutpat purus. Sed libero felis</li>
    </ul>
  </div>
</aside>

<footer class="abs footer">Copyright &nbsp;©&nbsp; 2018 Harrowvale Institute of Training. &nbsp; All rights reserved.</footer>
</body>
</html>
```